Laundromat wall mural with logo, wash steps and soap dish instructions

Hi,
I am building a new laundromat and want to design a large wall mural containing a few different sections. The first piece would be a large image of my logo "Suds Harbor Laundromat" with my new tag line under it "A better Place to Wash". The next section would be general washing instructions: (step1) load clothes, (step 2) load soap, (step 3) select cycle (step 4) present payment (Quarters, Credit Card or Fennix/trove pay) (Step 5) Press start. Please use the wave from the logo to encase each of these 5 steps. Also please use an emblem in each wave to show each sections action. Such as they did in one of the example files I attached to this brief. The Final section would be the design for the soap compartment, describing where it goes. Please place the title "Where does the soap go?" above this section. The whole wall section will be 40 feet wide and 5 feet tall. I would like each section to flow aesthetically into the other. Feel free to use the logos waves and colors to bring everything together. I have attached examples of other store designs that I have found. The design will be above the washers that are placed against the wall.
I also placed a design of the mural that I wasn't completely impressed with so I opened the project to more designers.

Please let me know what other info you need.

Bests

Target Market(s)

laundromat customers

Industry/Entity Type

Laundromat

Font styles to use
Sans Serif

Colors
0054AA
0677BA
7BADD7
CADEEF
E8F1F8

Requirements
Must have
• The wave from my logo continuously flowing around the side and bottom borders.

```html
<!DOCTYPE html>
<html lang="en">
<head>
<meta charset="utf-8">
<title>Suds Harbor Laundromat – Wall Mural</title>
<link rel="stylesheet" href="https://fonts.googleapis.com/css2?family=Exo+2:ital,wght@0,800;1,900&family=Oswald:wght@300;600&family=Poppins:wght@700&display=swap">
<style>
  :root{
    --navy:#0054AA;
    --blue:#0677BA;
    --sky:#7BADD7;
    --mist:#CADEEF;
    --ice:#E8F1F8;
    --ink:#0B3A82;
    --stage:#A6A6A6;
  }
  *{margin:0;padding:0;box-sizing:border-box}
  html,body{width:1200px;height:282px;overflow:hidden;background:var(--stage)}
  .mural{position:absolute;left:62px;top:64px;width:1064px;height:132px;overflow:hidden;
    background:linear-gradient(180deg,#fff 0%,var(--ice) 70%,var(--mist) 100%);
    box-shadow:0 2px 6px rgba(0,0,0,.35)}
  .layer{position:absolute;left:0;top:0}
  .brand{position:absolute;left:32px;top:26px;display:flex;align-items:center;gap:6px}
  .brand-dot{width:12px;height:12px;border-radius:50%;background:var(--blue)}
  .brand-name{font:800 15px/1 "Exo 2",sans-serif;color:var(--blue);letter-spacing:.3px}
  .brand-name small{display:block;font-size:7px;letter-spacing:2.6px;margin-top:2px}
  .tagline{position:absolute;left:24px;top:62px;font-family:"Exo 2",sans-serif;font-style:italic;font-weight:900;line-height:.95}
  .tagline .lead{display:block;font-size:15.5px;color:var(--blue)}
  .tagline .main{display:block;font-size:29px;color:var(--navy)}
  .step{position:absolute;top:0;width:110px;height:132px}
  .step-num{position:absolute;left:0;top:18px;font:300 60px/1 "Oswald",sans-serif;color:transparent;-webkit-text-stroke:1.2px var(--blue)}
  .step-label{position:absolute;left:var(--gap);top:29px;font:600 14px/1.08 "Oswald",sans-serif;color:var(--navy);text-transform:uppercase;white-space:nowrap}
  .soap-title{position:absolute;left:834px;top:34px;font-family:"Exo 2",sans-serif;font-style:italic;font-weight:900;line-height:1.08;font-size:18px;color:var(--ink)}
  .soap-title .accent{display:block;color:#fff;-webkit-text-stroke:.6px var(--navy);font-size:15px}
  .compartment{position:absolute;left:948px;top:8px;width:68px;height:124px;border-radius:6px 6px 0 0;
    background:linear-gradient(180deg,#7d8a97 0%,#5c6670 60%,#48515a 100%)}
  .soap-label{position:absolute;width:34px;font:700 4.6px/1.15 "Poppins",sans-serif;color:var(--ink);text-transform:uppercase;text-align:center}
</style>
</head>
<body>
<section class="mural" aria-label="Suds Harbor Laundromat washing instructions mural">
  <svg class="layer" width="1064" height="132" viewBox="0 0 1064 132">
    <defs>
      <linearGradient id="water" x1="0" y1="0" x2="0" y2="1">
        <stop offset="0" stop-color="#8fc3ee"/>
        <stop offset="1" stop-color="#1f7fd0"/>
      </linearGradient>
      <linearGradient id="water-light" x1="0" y1="0" x2="0" y2="1">
        <stop offset="0" stop-color="#d3e8f8"/>
        <stop offset="1" stop-color="#7BADD7"/>
      </linearGradient>
      <linearGradient id="panel" x1="0" y1="0" x2="1" y2="1">
        <stop offset="0" stop-color="#5e9fe0"/>
        <stop offset=".55" stop-color="#9fc8ee"/>
        <stop offset="1" stop-color="#CADEEF"/>
      </linearGradient>
    </defs>
    <path class="wave-back" d="M0 110 C60 96 110 120 170 110 S290 92 350 108 S470 122 540 104 S680 94 740 110 S800 116 840 104 L840 132 L0 132Z" fill="url(#water-light)"/>
    <path class="wave-front" d="M0 122 C50 110 120 128 190 118 S320 106 390 120 S520 128 600 114 S730 108 800 122 L840 116 L840 132 L0 132Z" fill="url(#water)"/>
    <g class="step-rings" fill="none" stroke="var(--blue)" stroke-width="1">
      <circle cx="255" cy="56" r="42"/>
      <circle cx="386" cy="56" r="42"/>
      <circle cx="514" cy="56" r="42"/>
      <circle cx="640" cy="56" r="42"/>
      <circle cx="764" cy="56" r="42"/>
    </g>
    <g class="emblem-discs" fill="var(--navy)" stroke="#fff" stroke-width="3">
      <circle cx="246" cy="94" r="21"/>
      <circle cx="378" cy="94" r="21"/>
      <circle cx="503" cy="94" r="21"/>
      <circle cx="634" cy="94" r="21"/>
      <circle cx="760" cy="94" r="21"/>
    </g>
    <g class="emblem-washer" transform="translate(246 94)">
      <rect x="-10" y="-11" width="20" height="22" rx="2" fill="#f2f2f2"/>
      <rect x="-10" y="-11" width="20" height="5" fill="#e0524a"/>
      <circle cx="0" cy="3" r="6" fill="#5ab6e8" stroke="#333" stroke-width="1"/>
    </g>
    <g class="emblem-bottle" transform="translate(378 94)">
      <path d="M-4 -10 h8 v4 l4 4 v14 h-16 v-14 l4-4z" fill="#f2f2f2"/>
      <rect x="-7" y="0" width="14" height="7" fill="#c06ad1"/>
    </g>
    <g class="emblem-pointer" transform="translate(503 94)">
      <path d="M-3 -10 a2 2 0 0 1 4 0 v9 l7 2 a3 3 0 0 1 2 4 l-2 6 h-10 l-5-7 a2 2 0 0 1 3-3 l1 1z" fill="#f6c48a" stroke="#333" stroke-width=".8"/>
    </g>
    <g class="emblem-payment" transform="translate(634 94)">
      <circle cx="2" cy="-4" r="7" fill="#f5c542" stroke="#333" stroke-width=".8"/>
      <text x="2" y="-1" font-family="Poppins,sans-serif" font-weight="700" font-size="8" text-anchor="middle" fill="#333">$</text>
      <path d="M-9 8 q6-5 12-1 h4 l4-3" fill="none" stroke="#f6c48a" stroke-width="3" stroke-linecap="round"/>
    </g>
    <g class="emblem-power" transform="translate(760 94)" fill="none" stroke-linecap="round">
      <circle r="13" fill="#bfe6f7"/>
      <path d="M-5 -5 a7 7 0 1 0 10 0" stroke="var(--navy)" stroke-width="2"/>
      <path d="M0 -8 v7" stroke="var(--navy)" stroke-width="2"/>
    </g>
    <path class="soap-panel" d="M832 0 Q804 66 820 132 L1064 132 L1064 0Z" fill="url(#panel)"/>
    <path class="soap-panel-edge" d="M832 0 Q804 66 820 132" fill="none" stroke="var(--navy)" stroke-width="4"/>
  </svg>

  <div class="brand">
    <span class="brand-dot"></span>
    <p class="brand-name">SUDS HARBOR<small>LAUNDROMAT</small></p>
  </div>
  <h1 class="tagline"><span class="lead">A BETTER PLACE</span><span class="main">TO WASH</span></h1>

  <div class="step" style="left:190px;--gap:28px"><span class="step-num">1</span><p class="step-label">Load<br>Clothes</p></div>
  <div class="step" style="left:318px;--gap:37px"><span class="step-num">2</span><p class="step-label">Load<br>Soap</p></div>
  <div class="step" style="left:450px;--gap:36px"><span class="step-num">3</span><p class="step-label">Select<br>Cycle</p></div>
  <div class="step" style="left:575px;--gap:38px"><span class="step-num">4</span><p class="step-label">Present<br>Payment</p></div>
  <div class="step" style="left:698px;--gap:40px"><span class="step-num">5</span><p class="step-label">Press<br>Start</p></div>

  <h2 class="soap-title">WHERE<br>DOES THE<span class="accent">SOAP GO?</span></h2>
  <div class="compartment" role="img" aria-label="Photo of the washer soap compartment with its dispenser slots"></div>

  <svg class="layer" width="1064" height="132" viewBox="0 0 1064 132">
    <g class="soap-guides" fill="none" stroke="#2f86d6" stroke-width="4" stroke-linecap="round">
      <path d="M938 62 q16-6 28 6"/>
      <path d="M938 90 q16 6 28-6"/>
      <path d="M1024 62 q-16-6 -28 6"/>
      <path d="M1024 90 q-16 6 -28-6"/>
    </g>
    <g class="soap-icons" fill="var(--navy)" stroke="#fff" stroke-width="1">
      <circle cx="928" cy="64" r="7"/>
      <circle cx="928" cy="88" r="7"/>
      <circle cx="1034" cy="64" r="7"/>
      <circle cx="1034" cy="88" r="7"/>
    </g>
    <g fill="none" stroke="#fff" stroke-width=".9">
      <circle cx="928" cy="64" r="2.5"/>
      <path d="M924 86 v4 h8 v-4"/>
      <path d="M1031 61 l6 6 M1037 61 l-6 6"/>
      <path d="M1030 86 v4 h8 v-4"/>
    </g>
  </svg>
  <span class="soap-label" style="left:911px;top:44px">Fabric<br>Soften</span>
  <span class="soap-label" style="left:911px;top:98px">Detergent</span>
  <span class="soap-label" style="left:1017px;top:44px">Liquid only<br>Detergent</span>
  <span class="soap-label" style="left:1017px;top:98px">Detergent</span>
</section>
</body>
</html>
```